Ferrant Valley Zoning Council Business Cards

We're looking for a business card design, simple as that. We're a local government agency that mainly performs building code enforcement, transportation planning, floodplain management, and GIS for Tobelle Parish in Louisiana, and other surround parishes. So you're not having to Google anything, GIS is, at it's core, mapping. Building Code Enforcement is just that, nothing more. Floodplain Management is to make sure the public is within what the government

Contact Information for Business Card

Our Address is

517 Marwick Street
Alexandria, LA 71489

Our phone is 3185529137
Our fax is 3185529142
Our website is www.fvzc.info
My email is dana@fvzc.info

Font styles to use
Serif
Sans Serif

Colors

Designer to choose colors to be used in the design.

Requirements
Must have
• I'm attaching our logo(several versions) that must be incorporated. The design should fit well with our existing logo. I can send photoshop files for our logo if needed. If possible, I'd like to be able to add names/info to each card for all of our employees once this is done.
Nice to have
• The Louisiana state seal is a bonus, and isn't specifically required.

```html
<!DOCTYPE html>
<html lang="en">
<head>
<meta charset="utf-8">
<title>Ferrant Valley Zoning Council — Business Cards</title>
<link href="https://fonts.googleapis.com/css2?family=Open+Sans:wght@400;600;700&display=swap" rel="stylesheet">
<style>
  :root {
    --stage: #e4e4e4;
    --card-dark: #1e1e1e;
    --card-light: #f4f4f4;
    --ink: #1b1b1b;
    --ink-light: #ffffff;
    --accent-blue: #3d4ea8;
    --accent-orange: #e88b22;
    --accent-green: #27a844;
    --accent-lime: #c8d62a;
    --rule: #2a2a2a;
  }
  * { box-sizing: border-box; margin: 0; padding: 0; }
  html, body { width: 1200px; height: 1021px; overflow: hidden; }
  body {
    background: var(--stage);
    font-family: "Open Sans", Arial, sans-serif;
    position: relative;
  }
  .card {
    position: absolute;
    left: 250px;
    width: 700px;
    height: 400px;
    overflow: hidden;
    box-shadow: 0 6px 18px rgba(0,0,0,.18);
  }
  .card--back { top: 70px; background: var(--card-dark); }
  .card--front { top: 540px; background: var(--card-light); color: var(--ink); }

  .stripe {
    position: absolute; left: 0; right: 0; bottom: 0; height: 14px;
    display: flex;
  }
  .stripe span { flex: 1; }
  .stripe .blue { background: var(--accent-blue); }
  .stripe .orange { background: var(--accent-orange); }
  .stripe .green { background: var(--accent-green); }
  .stripe .lime { background: var(--accent-lime); }

  .brand {
    display: flex; align-items: center; gap: 14px;
    font-weight: 700; letter-spacing: .5px;
  }
  .brand__mark { width: 22px; height: 22px; background: var(--accent-green); flex: none; }
  .card--back .brand {
    position: absolute; left: 0; right: 0; top: 172px; justify-content: center;
    color: var(--ink-light); font-size: 34px;
  }
  .card--front .brand {
    position: absolute; left: 40px; top: 44px;
    color: var(--ink); font-size: 24px;
  }
  .card--front .brand__mark { width: 18px; height: 18px; }

  .divider {
    position: absolute; left: 52px; width: 560px; top: 214px;
    border-top: 1.5px solid var(--rule);
  }
  .seal {
    position: absolute; left: 552px; top: 62px;
  }
  .contact {
    position: absolute; left: 40px; top: 228px;
    list-style: none; font-size: 19px; line-height: 27px;
  }
  .contact li { display: flex; align-items: center; gap: 8px; }
  .contact svg { width: 16px; height: 16px; flex: none; }

  .person {
    position: absolute; right: 60px; top: 172px; text-align: right;
  }
  .person__name { font-size: 26px; font-weight: 700; color: var(--accent-blue); line-height: 36px; }
  .person__role { font-size: 19px; line-height: 32px; }

  .address {
    position: absolute; right: 60px; top: 292px; text-align: right;
    font-size: 21px; line-height: 28px;
  }
</style>
</head>
<body>

  <section class="card card--back" aria-label="Card back">
    <div class="brand"><span class="brand__mark"></span>Ferrant Valley Zoning Council</div>
    <div class="stripe"><span class="blue"></span><span class="orange"></span><span class="green"></span><span class="lime"></span></div>
  </section>

  <section class="card card--front" aria-label="Card front">
    <div class="brand"><span class="brand__mark"></span>Ferrant Valley Zoning Council</div>

    <svg class="seal" width="116" height="116" viewBox="0 0 116 116" aria-hidden="true">
      <circle cx="58" cy="58" r="56" fill="#ffffff" stroke="#1d3f8a" stroke-width="4"/>
      <circle cx="58" cy="58" r="40" fill="#1d3f8a"/>
    </svg>

    <div class="divider"></div>

    <ul class="contact">
      <li>
        <svg viewBox="0 0 16 16" aria-hidden="true"><path fill="var(--accent-orange)" d="M3.6 1.2l2.4 2.9-1.3 1.6c.9 2 2.6 3.7 4.6 4.6l1.6-1.3 2.9 2.4-1.3 2.2C7.2 13.6 2.4 8.8 1.4 3.5z"/></svg>
        318-552-9137
      </li>
      <li>
        <svg viewBox="0 0 16 16" aria-hidden="true"><g fill="var(--accent-orange)"><rect x="4" y="1" width="8" height="4"/><rect x="1" y="5" width="14" height="6" rx="1"/><rect x="4" y="10" width="8" height="5" fill="#fff" stroke="var(--accent-orange)" stroke-width="1.4"/></g></svg>
        318-552-9142
      </li>
      <li>
        <svg viewBox="0 0 16 16" aria-hidden="true"><rect x="1" y="3" width="14" height="10" fill="none" stroke="var(--accent-orange)" stroke-width="1.6"/><path d="M1 3l7 6 7-6" fill="none" stroke="var(--accent-orange)" stroke-width="1.6"/></svg>
        dana@fvzc.info
      </li>
      <li>
        <svg viewBox="0 0 16 16" aria-hidden="true"><g fill="none" stroke="var(--accent-orange)" stroke-width="1.4"><circle cx="8" cy="8" r="6.5"/><ellipse cx="8" cy="8" rx="3" ry="6.5"/><path d="M1.5 8h13"/></g></svg>
        www.fvzc.info
      </li>
    </ul>

    <div class="person">
      <div class="person__name">Theo Marchand</div>
      <div class="person__role">Founder</div>
    </div>

    <address class="address" style="font-style:normal">
      517 Marwick Street<br>Alexandria, LA 71489
    </address>

    <div class="stripe"><span class="blue"></span><span class="orange"></span><span class="green"></span><span class="lime"></span></div>
  </section>

</body>
</html>
```